Website Update for Global Company - Solar Technology - Brisqell

We recently released our first version of our website kelvaris.com. However despite a longer process of developing the page, it is still missing the elements of a brilliant website. (Currently it looks dead and boring) We are having problems integrating our logo and want to create a more catching site. The task involves an updated and without changing most of main elements in the existing page. (Unless you can do it even better) The blue color needs to be kept but can be changed within the blue-spectrum. The logo text (KELVARIS) must be better integrated in the site, however the main logo could be used in elements like we have tried with the background. The surface of the logo could be changed to 3D or metallic, or any other theme that would make the site more complete.
It would be good if some elements of the site could be used on business cards and invoices to keep the company identity.
Kelvaris is a new development company specialized in green energy and sustainable development. We do design, engineering, manufacturing, sourcing and other processes related to product development – both as consultants and for own products.
Keep the look of the site as professional as possible, and with a cooperate-looking style.

Link to existing page: www.kelvaris.com

Brief Update : After reviewing the designs we would like all new and current designers to make more bold designs that stands out from the rest. We do not like the standard layout that looks like any other cooperate homepage. We want a very unique and very lively page - with faded images and effects when hoovering like seen on our existing page. Try make all elements blend together, and use faded background images instead of just white color - or something else.

Make the site unique !

Industry/Entity Type

Solar Energy

Contact Information for Business Card

Owner/Founder/CEO : Frederik Lysgaard Holm
Company name: Kelvaris ApS
Email: frederik.lysgaard@kelvaris.dk
Phone: +45 71 83 96 54
Slogan Sustainable Development
Address: Havnestien 18, 2
DK-5820 Svendborg, Denmark

Number of Pages Required

3 page

Font styles to use
Serif
Sans Serif

Colors
0555a3
85acd3
cedeed
3176b5
cee9f5
85cae6
0293ce
86cfc6
33b8a4

```html
<!DOCTYPE html>
<html lang="en">
<head>
<meta charset="utf-8">
<title>Kelvaris – Green Energy &amp; Sustainable Development</title>
<link href="https://fonts.googleapis.com/css2?family=Open+Sans:wght@400;600;700&family=Oswald:wght@500;700&display=swap" rel="stylesheet">
<style>
:root{
  --blue:#0293ce;
  --blue-deep:#0555a3;
  --blue-mid:#3176b5;
  --blue-soft:#85cae6;
  --blue-pale:#cee9f5;
  --ink:#333;
  --muted:#8a8a8a;
  --light:#f1f1f1;
  --line:#e2e2e2;
  --foot:#2c2c2c;
  --foot-bar:#1f1f1f;
  --foot-text:#9a9a9a;
}
*{box-sizing:border-box;margin:0;padding:0}
html,body{width:1200px;height:2200px;overflow:hidden}
body{font-family:"Open Sans",Arial,sans-serif;color:var(--ink);background:#fff;position:relative}
a{color:inherit;text-decoration:none}

/* header */
.site-header{position:absolute;top:0;left:0;width:1200px;height:70px;background:#fff;display:flex;align-items:center;justify-content:space-between;padding:0 40px;box-shadow:0 1px 4px rgba(0,0,0,.08);z-index:2}
.brand{display:flex;align-items:center;gap:12px}
.brand-mark{width:34px;height:34px;background:var(--ink)}
.brand-name{font-weight:700;font-size:24px;letter-spacing:1px;color:var(--ink)}
.main-nav{display:flex;gap:6px}
.main-nav a{font-size:11px;font-weight:600;padding:8px 14px;color:#555;letter-spacing:.5px}
.main-nav a.is-active{color:var(--blue);border-bottom:2px solid var(--blue)}

/* hero */
.hero{position:absolute;top:70px;left:0;width:1200px;height:530px;
  background:
    radial-gradient(ellipse 520px 260px at 78% 30%,rgba(245,248,252,.75),rgba(245,248,252,0) 70%),
    radial-gradient(ellipse 700px 300px at 55% 85%,rgba(133,202,230,.55),rgba(133,202,230,0) 70%),
    radial-gradient(ellipse 500px 400px at 10% 20%,rgba(40,60,80,.55),rgba(40,60,80,0) 70%),
    linear-gradient(165deg,#5d7891 0%,#a7bccf 40%,#4f7aa6 70%,#1c3c63 100%)}
.hero-title{position:absolute;left:40px;top:300px;font-family:"Oswald",Impact,sans-serif;font-weight:500;font-size:40px;line-height:1.35;color:#fff}
.hero-title span{display:inline-block;background:rgba(25,30,38,.85);padding:2px 16px;margin-bottom:6px}
.slide-arrow{position:absolute;top:240px;width:36px;height:50px;background:rgba(0,0,0,.35);display:flex;align-items:center;justify-content:center}
.slide-arrow.prev{left:0}.slide-arrow.next{right:0}

/* sections */
.section-title{text-align:center;font-size:30px;font-weight:600;color:var(--ink);letter-spacing:1px}
.section-sub{text-align:center;font-size:10px;color:var(--muted);letter-spacing:.5px;margin-top:14px}
.services{position:absolute;top:600px;left:0;width:1200px;height:460px;padding-top:50px}
.service-list{display:flex;justify-content:center;gap:40px;margin-top:55px}
.service{width:220px;text-align:center}
.service-icon{width:84px;height:84px;border-radius:50%;border:2px solid var(--blue);margin:0 auto;display:flex;align-items:center;justify-content:center}
.service-icon.is-filled{background:var(--blue)}
.service h3{font-size:12px;font-weight:600;color:var(--blue);margin:22px 0 10px;letter-spacing:.5px}
.service p{font-size:11px;color:var(--muted);line-height:1.6}

.media{position:absolute;top:1060px;left:0;width:1200px;height:380px;background:var(--light);display:flex;gap:60px;padding:40px 60px}
.media h2{font-size:18px;font-weight:400;color:var(--ink);padding-bottom:10px;border-bottom:1px solid var(--line);margin-bottom:16px}
.videos{width:600px}
.video-frame{height:260px;position:relative;
  background:
    radial-gradient(ellipse 200px 120px at 78% 45%,rgba(230,236,242,.8),rgba(230,236,242,0) 70%),
    radial-gradient(ellipse 220px 200px at 18% 40%,rgba(70,80,95,.7),rgba(70,80,95,0) 70%),
    linear-gradient(180deg,#d9dee4 0%,#a9b3be 55%,#4a5663 100%)}
.play{position:absolute;left:50%;top:50%;width:60px;height:42px;margin:-21px 0 0 -30px;background:#d8281f;border-radius:10px;display:flex;align-items:center;justify-content:center}
.news{flex:1}
.news-item{margin-bottom:18px}
.news-item h4{font-size:12px;font-weight:600;color:var(--ink)}
.news-item time{display:block;font-size:10px;color:var(--blue);margin:4px 0}
.news-item p{font-size:11px;color:var(--muted);line-height:1.5}
.news-item .more{font-size:10px;color:var(--ink);margin-top:6px;display:block}

.work{position:absolute;top:1440px;left:0;width:1200px;height:420px;padding-top:55px}
.work-list{display:flex;justify-content:center;gap:20px;margin-top:40px;position:relative}
.work-card{width:340px;height:200px;position:relative}
.work-card figcaption{position:absolute;left:0;right:0;bottom:0;height:34px;background:rgba(5,85,163,.8);color:#fff;font-size:13px;display:flex;align-items:center;justify-content:center}
.work-a{background:radial-gradient(ellipse 140px 110px at 50% 40%,#eef5fb,rgba(238,245,251,0) 75%),linear-gradient(135deg,#9cb7d2,#3f6d9b)}
.work-b{background:radial-gradient(ellipse 150px 60px at 50% 50%,#9ea3a8,rgba(158,163,168,0) 75%),linear-gradient(135deg,#fafafa,#d6d8da)}
.work-c{background:radial-gradient(ellipse 110px 120px at 55% 40%,rgba(220,170,140,.55),rgba(220,170,140,0) 75%),linear-gradient(135deg,#8aa2ba,#2a4766)}
.work-arrow{position:absolute;top:80px;width:26px;height:40px;background:rgba(0,0,0,.25);display:flex;align-items:center;justify-content:center}
.work-arrow.prev{left:60px}.work-arrow.next{right:60px}

/* footer */
.site-footer{position:absolute;top:1860px;left:0;width:1200px;height:300px;background:var(--foot);display:flex;gap:40px;padding:40px 60px;color:var(--foot-text)}
.site-footer h5{font-size:12px;color:#fff;font-weight:600;margin-bottom:16px;letter-spacing:.5px}
.foot-col{width:220px}
.link-grid{display:grid;grid-template-columns:1fr 1fr;gap:10px 10px;font-size:10px}
.link-list{display:grid;gap:10px;font-size:10px}
.contact-col{flex:1}
.subscribe{display:flex}
.subscribe span{flex:1;height:30px;background:#fff;color:#aaa;font-size:10px;padding:0 10px;display:flex;align-items:center}
.subscribe b{height:30px;background:var(--blue);color:#fff;font-size:10px;font-weight:600;padding:0 14px;display:flex;align-items:center}
.foot-brand{font-size:22px;font-weight:700;color:#fff;letter-spacing:1px;margin:22px 0 10px}
.foot-row{display:flex;justify-content:space-between;align-items:center;font-size:11px}
.socials{display:flex;gap:8px}
.socials i{width:22px;height:22px;border-radius:50%;background:var(--blue-mid);display:block}
.foot-bar{position:absolute;top:2160px;left:0;width:1200px;height:40px;background:var(--foot-bar);color:var(--foot-text);font-size:10px;display:flex;align-items:center;padding:0 60px}
</style>
</head>
<body>

<header class="site-header">
  <div class="brand"><div class="brand-mark"></div><span class="brand-name">KELVARIS</span></div>
  <nav class="main-nav">
    <a class="is-active">HOME</a><a>WORK</a><a>EXPERTISE</a><a>APPROACH</a><a>CLIENTS</a><a>ABOUT</a><a>CONTACT</a>
  </nav>
</header>

<section class="hero" role="img" aria-label="Photo of hands typing on a keyboard with a blue digital network overlay">
  <h1 class="hero-title"><span>Green Energy &amp; Sustainable</span><br><span>Development..!</span></h1>
  <div class="slide-arrow prev"><svg width="12" height="18" viewBox="0 0 12 18"><path d="M10 1 2 9l8 8" stroke="#fff" stroke-width="2.5" fill="none"/></svg></div>
  <div class="slide-arrow next"><svg width="12" height="18" viewBox="0 0 12 18"><path d="M2 1l8 8-8 8" stroke="#fff" stroke-width="2.5" fill="none"/></svg></div>
</section>

<section class="services">
  <h2 class="section-title">WHAT WE DO?</h2>
  <p class="section-sub">SIMPLE CLEAR ENERGY SOLUTIONS FROM CONCEPT TO PRODUCT. WE BUILD WITH CARE FOR PEOPLE AND THE PLANET.</p>
  <div class="service-list">
    <div class="service">
      <div class="service-icon is-filled"><svg width="36" height="32" viewBox="0 0 36 32"><rect x="2" y="2" width="32" height="21" rx="2" fill="none" stroke="#fff" stroke-width="3"/><path d="M12 30h12M18 23v7" stroke="#fff" stroke-width="3"/></svg></div>
      <h3>DESIGN</h3>
      <p>We shape early ideas into clear concepts, tested with care and built for real use.</p>
    </div>
    <div class="service">
      <div class="service-icon"><svg width="36" height="36" viewBox="0 0 36 36"><circle cx="14" cy="14" r="8" fill="none" stroke="#0293ce" stroke-width="3"/><circle cx="14" cy="14" r="2.5" fill="#0293ce"/><circle cx="27" cy="27" r="5" fill="none" stroke="#0293ce" stroke-width="3"/></svg></div>
      <h3>ENGINEERING</h3>
      <p>Our engineers turn concepts into robust systems that perform well in every season.</p>
    </div>
    <div class="service">
      <div class="service-icon"><svg width="36" height="36" viewBox="0 0 36 36"><rect x="4" y="15" width="16" height="9" rx="4.5" transform="rotate(-45 12 19.5)" fill="none" stroke="#0293ce" stroke-width="3"/><rect x="16" y="12" width="16" height="9" rx="4.5" transform="rotate(-45 24 16.5)" fill="none" stroke="#0293ce" stroke-width="3"/></svg></div>
      <h3>MANUFACTURING</h3>
      <p>We plan production runs with trusted partners to keep quality high and waste low.</p>
    </div>
    <div class="service">
      <div class="service-icon"><svg width="30" height="38" viewBox="0 0 30 38"><path d="M15 3a11 11 0 0 0-6 20v5h12v-5a11 11 0 0 0-6-20z" fill="none" stroke="#0293ce" stroke-width="3"/><path d="M10 33h10" stroke="#0293ce" stroke-width="3"/></svg></div>
      <h3>SOURCING</h3>
      <p>We find reliable suppliers and fair materials so every part meets our standard.</p>
    </div>
  </div>
</section>

<section class="media">
  <div class="videos">
    <h2>Project Videos</h2>
    <div class="video-frame" role="img" aria-label="Video still of a laptop with abstract geometric shapes">
      <div class="play"><svg width="16" height="18" viewBox="0 0 16 18"><path d="M1 1l14 8-14 8z" fill="#fff"/></svg></div>
    </div>
  </div>
  <div class="news">
    <h2>In The News</h2>
    <article class="news-item">
      <h4>Solar panel pilot now running in Odense</h4>
      <time>August 17, 2015</time>
      <p>Our first field test is live and early results show a steady rise in output.</p>
      <a class="more">› Read More</a>
    </article>
    <article class="news-item">
      <h4>New partner joins our sourcing network</h4>
      <time>August 12, 2015</time>
      <p>We welcome a supplier of recycled aluminium frames for our next product line.</p>
      <a class="more">› Read More</a>
    </article>
  </div>
</section>

<section class="work">
  <h2 class="section-title">OUR WORK</h2>
  <p class="section-sub">SELECTED PROJECTS IN DESIGN, ENGINEERING AND MANUFACTURING FOR CLIENTS WHO CARE ABOUT A GREENER FUTURE.</p>
  <div class="work-list">
    <figure class="work-card work-a" role="img" aria-label="Light bulb with glowing innovation icons"><figcaption>Focused Innovation</figcaption></figure>
    <figure class="work-card work-b" role="img" aria-label="Pencil sketch of a concept sports car"><figcaption>Industrial Design</figcaption></figure>
    <figure class="work-card work-c" role="img" aria-label="Engineer working at a machine in a workshop"><figcaption>Mechanical Engineering</figcaption></figure>
    <div class="work-arrow prev"><svg width="10" height="16" viewBox="0 0 10 16"><path d="M8 1 2 8l6 7" stroke="#fff" stroke-width="2" fill="none"/></svg></div>
    <div class="work-arrow next"><svg width="10" height="16" viewBox="0 0 10 16"><path d="M2 1l6 7-6 7" stroke="#fff" stroke-width="2" fill="none"/></svg></div>
  </div>
</section>

<footer class="site-footer">
  <div class="foot-col">
    <h5>QUICK LINKS</h5>
    <div class="link-grid"><a>› Home</a><a>› Clients</a><a>› Work</a><a>› About</a><a>› Expertise</a><a>› Contact</a><a>› Approach</a><a>› Careers</a></div>
  </div>
  <div class="foot-col">
    <h5>EXPERTISE</h5>
    <div class="link-grid"><a>› Design</a><a>› Sourcing</a><a>› Engineering</a><a>› Consulting</a><a>› Manufacturing</a><a>› Prototyping</a></div>
  </div>
  <div class="foot-col" style="width:160px">
    <h5>ABOUT</h5>
    <div class="link-list"><a>› Company</a><a>› History</a><a>› Careers</a><a>› Team</a></div>
  </div>
  <div class="contact-col">
    <h5>CONTACT US</h5>
    <div class="subscribe"><span>Your email</span><b>SUBSCRIBE</b></div>
    <div class="foot-brand">KELVARIS</div>
    <div class="foot-row">
      <div class="socials"><i></i><i></i><i></i><i></i><i></i></div>
      <span>+45 71 83 96 54</span>
    </div>
  </div>
</footer>
<div class="foot-bar">© 2015 Kelvaris. All Rights Reserved.</div>

</body>
</html>
```